Keldro Cybersecurity Secives professional web site

Keldro is a unit of the Vostemic company, based on the audit services it offers and which mainly works by the contacts it has from its previous experience. The objective with the development of this website will be to increase its presence on the internet and even link the traffic of its social networks with the blog of the new page and in this way, provide information for old and potential customers.
For this reason, we will set the objective of the page, have all the information of the company, its services and its scope in general, in a formal and simple for users, facilitating the task of finding the information they want within of the page, as well as, including the option of feedback.
Updates

Need extra days to review

Target Market(s)

any company that needs security assessments

Number of Pages Required

4 page

Font styles to use
Sans Serif

Colors

Designer to choose colors to be used in the design.

Requirements
Must have
• READ THE PDF PLEASE. Video in homepage, cool graphics, color like our logo
• I like the following sites: www.vostemic-example.com & www.gantrelo-example.com
Nice to have
• Futuristic
Should not have
• Please, dont use the gallery pictures I used in my document, I prefer hand made illustrations instead

```html
<!DOCTYPE html>
<html lang="en">
<head>
<meta charset="utf-8">
<title>Keldro Security</title>
<link rel="stylesheet" href="https://fonts.googleapis.com/css2?family=Raleway:wght@600;700;800&family=Arimo:wght@400&display=swap">
<style>
  :root {
    --navy: #07077d;
    --white: #ffffff;
    --card-border: #d6d6d6;
    --body-text: #666666;
    --ring: #f1f1f1;
    --progress: #e0161a;
    --bar-dark: #2c3a5c;
  }
  * { box-sizing: border-box; margin: 0; padding: 0; }
  html, body { width: 1200px; height: 604px; overflow: hidden; background: var(--white); }
  body { position: relative; font-family: "Arimo", Arial, sans-serif; }

  .site-header { position: absolute; left: 0; top: 0; width: 1200px; height: 82px; background: var(--navy); }
  .brand { position: absolute; left: 34px; top: 12px; display: flex; align-items: center; gap: 10px; }
  .brand-name { font-family: "Raleway", Arial, sans-serif; font-weight: 800; color: var(--white); font-size: 23px; line-height: 21px; text-align: right; letter-spacing: .3px; }
  .brand-mark { width: 54px; height: 54px; border-radius: 50%; background: var(--white); }

  .language { position: absolute; top: 9px; left: 933px; display: flex; align-items: center; gap: 10px; }
  .language-label { font-family: "Raleway", Arial, sans-serif; font-weight: 700; font-size: 9.5px; color: var(--white); letter-spacing: .3px; }
  .language-select { width: 131px; height: 22px; background: #f4f4f6; display: flex; align-items: center; padding: 0 8px; gap: 6px; font-size: 8px; color: #8a8a9a; font-family: "Raleway", Arial, sans-serif; font-weight: 600; }
  .language-flag { width: 14px; height: 9px; background: #c4ccdd; }
  .language-select svg { margin-left: auto; }

  .main-nav { position: absolute; top: 58px; left: 856px; display: flex; gap: 0; }
  .main-nav a { font-family: "Raleway", Arial, sans-serif; font-weight: 700; font-size: 11.5px; color: var(--white); text-decoration: none; position: absolute; white-space: nowrap; }

  .feature { position: absolute; top: 149px; width: 161px; height: 301px; }
  .feature::before { content: ""; position: absolute; left: 3px; top: -3px; width: 161px; height: 301px; border: 1px solid var(--card-border); background: var(--white); }
  .feature-card { position: absolute; inset: 0; border: 1px solid var(--card-border); background: var(--white); }
  .feature-photo { position: absolute; left: 16px; top: 17px; width: 128px; height: 128px; border-radius: 50%; background: var(--ring); box-shadow: 0 0 4px rgba(0,0,0,.12); }
  .feature-photo span { position: absolute; left: 10px; top: 10px; width: 108px; height: 108px; border-radius: 50%; display: block; }
  .feature-text { position: absolute; left: 8px; right: 8px; top: 157px; font-size: 11.6px; line-height: 17.3px; color: var(--body-text); text-align: center; }

  .video-player { position: absolute; left: 733px; top: 150px; width: 432px; height: 300px; border-radius: 8px; overflow: hidden; box-shadow: 0 1px 4px rgba(0,0,0,.35); }
  .video-frame { position: absolute; inset: 0; background: linear-gradient(135deg, #0e1a2e 0%, #3a5274 35%, #8fa3c0 60%, #5d6f8c 80%, #1f2b3f 100%); }
  .video-overlay { position: absolute; inset: 0; }

  .site-footer { position: absolute; left: 0; top: 529px; width: 1200px; height: 75px; background: var(--navy); }
  .footer-nav a { position: absolute; top: 52px; font-family: "Raleway", Arial, sans-serif; font-weight: 600; font-size: 9.5px; color: var(--white); text-decoration: none; }
  .social { position: absolute; top: 15px; width: 28px; height: 28px; border-radius: 50%; border: 1.5px solid var(--white); }
</style>
</head>
<body>
  <header class="site-header">
    <div class="brand">
      <div class="brand-name">KELDRO<br>SECURITY</div>
      <div class="brand-mark"></div>
    </div>
    <div class="language">
      <span class="language-label">SELECT LANGUAGE:</span>
      <div class="language-select">
        <span class="language-flag"></span>ENGLISH
        <svg width="10" height="6" viewBox="0 0 10 6"><path d="M1 1l4 4 4-4" fill="none" stroke="#8a8a9a" stroke-width="1.5"/></svg>
      </div>
    </div>
    <nav class="main-nav">
      <a href="#" style="left:0">COMPANY</a>
      <a href="#" style="left:95px">SERVICE</a>
      <a href="#" style="left:181px">BLOG</a>
      <a href="#" style="left:254px">CONTACT</a>
    </nav>
  </header>

  <main>
    <article class="feature" style="left:34px">
      <div class="feature-card">
        <div class="feature-photo"><span role="img" aria-label="Illustration of a glowing blue digital globe" style="background:radial-gradient(circle at 45% 45%, #3b7be0, #0c1fa8 60%, #051055)"></span></div>
        <p class="feature-text">Experts in cybersecurity. Protect your digital asset. We audit your company. Excellent&nbsp; reputation<br>.</p>
      </div>
    </article>
    <article class="feature" style="left:204px">
      <div class="feature-card">
        <div class="feature-photo"><span role="img" aria-label="Illustration of a security analyst working at monitors" style="background:radial-gradient(circle at 50% 40%, #3a6ad0, #10226e 60%, #060a30)"></span></div>
        <p class="feature-text">Our team will detect all your vulnerabilities. We offer the best services. We have extensive experience. Results guarantee.</p>
      </div>
    </article>
    <article class="feature" style="left:374px">
      <div class="feature-card">
        <div class="feature-photo"><span role="img" aria-label="Illustration of a hand touching a digital fingerprint scanner" style="background:radial-gradient(circle at 50% 50%, #d9b2a0, #8fb6dc 55%, #2e5da8)"></span></div>
        <p class="feature-text">We have the best technologies and innovations in cybersecurity. We manage your problems in the fastest and most economical way, thanks to our remote service.</p>
      </div>
    </article>
    <article class="feature" style="left:544px">
      <div class="feature-card">
        <div class="feature-photo"><span role="img" aria-label="Illustration of a hacker silhouette over a world map" style="background:radial-gradient(circle at 50% 55%, #6a88d8, #2447c6 65%, #a0262e)"></span></div>
        <p class="feature-text">We help you to know the ways to protect your company.<br>We offer you a personal treatment and the best advice with the necessary services for you</p>
      </div>
    </article>

    <section class="video-player" aria-label="Company video">
      <div class="video-frame" role="img" aria-label="Video still of a combination padlock resting on a laptop keyboard"></div>
      <svg class="video-overlay" width="432" height="300" viewBox="0 0 432 300">
        <circle cx="219" cy="120" r="35" fill="#ffffff" fill-opacity=".18" stroke="#ffffff" stroke-opacity=".35" stroke-width="3"/>
        <path d="M208 100v40l32-20z" fill="#ffffff" fill-opacity=".4"/>
        <g fill="#2b3550" stroke="#c9d2e4" stroke-width="1.5">
          <circle cx="407" cy="41" r="10"/><circle cx="407" cy="72" r="10"/>
          <circle cx="407" cy="102" r="10"/><circle cx="407" cy="132" r="10"/>
        </g>
        <g fill="none" stroke="#ffffff" stroke-width="1.4">
          <path d="M407 35l1.8 4 4.2.4-3.2 2.8 1 4.2-3.8-2.2-3.8 2.2 1-4.2-3.2-2.8 4.2-.4z" fill="#ffffff"/>
          <path d="M402 70a5 5 0 0 1 9-2M412 74a5 5 0 0 1-9 2"/>
          <rect x="401" y="98" width="12" height="8" rx="2"/>
          <circle cx="407" cy="132" r="5"/><path d="M407 129v3h2.5"/>
        </g>
        <rect x="7" y="264" width="418" height="29" rx="5" fill="#34426a" stroke="#9aa8c8" stroke-width="1"/>
        <path d="M33 265v27M78 265v27M389 265v27" stroke="#1c2540" stroke-width="1"/>
        <path d="M17 272v14l11-7z" fill="#ffffff"/>
        <path d="M49 276h3l4-3v12l-4-3h-3z" fill="#ffffff"/>
        <path d="M59 276a4 4 0 0 1 0 6M62 274a7 7 0 0 1 0 10" fill="none" stroke="#ffffff" stroke-width="1.2"/>
        <rect x="92" y="276" width="289" height="6" rx="3" fill="#0e1422"/>
        <rect x="92" y="276" width="121" height="6" rx="3" fill="var(--progress)"/>
        <circle cx="213" cy="279" r="6" fill="#7d8fb3" stroke="#dde4f2" stroke-width="1.5"/>
        <rect x="401" y="273" width="11" height="11" fill="none" stroke="#ffffff" stroke-width="1.4"/>
        <path d="M404 281l5-5M406 276h3v3" fill="none" stroke="#ffffff" stroke-width="1.2"/>
      </svg>
    </section>
  </main>

  <footer class="site-footer">
    <span class="social" style="left:535px" aria-label="Blog"></span>
    <span class="social" style="left:570px" aria-label="Social network"></span>
    <span class="social" style="left:604px" aria-label="Photo network"></span>
    <nav class="footer-nav">
      <a href="#" style="left:473px">COMPANY</a>
      <a href="#" style="left:553px">SERVICE</a>
      <a href="#" style="left:625px">BLOG</a>
      <a href="#" style="left:686px">CONTACT</a>
    </nav>
  </footer>
</body>
</html>
```